Birch Landing

HI We need book cover design done for a physical book. See the attached document that represents the text that we want.

The book is about retiring with financial freedom.

```html
<!DOCTYPE html>
<html lang="en">
<head>
<meta charset="utf-8">
<title>Freedom to Enjoy — Book Cover</title>
<link rel="stylesheet" href="https://fonts.googleapis.com/css2?family=Bodoni+Moda:wght@400;500&family=Libre+Caslon+Text&family=Playfair+Display:wght@400&display=swap">
<style>
  :root {
    --page: #ffffff;
    --navy-deep: #0a1140;
    --navy: #142266;
    --navy-light: #25388a;
    --slate: #6f7ba6;
    --maroon: #4a1838;
    --ink-light: #ffffff;
    --rule-red: #c8202a;
    --rule-light: #c9cde0;
  }
  html, body {
    margin: 0;
    width: 1200px;
    height: 1200px;
    overflow: hidden;
    background: var(--page);
  }
  .canvas { display: block; width: 1200px; height: 1200px; }
  .title-word { font-family: "Bodoni Moda", serif; font-weight: 500; fill: var(--ink-light); }
  .title-joiner { font-family: "Bodoni Moda", serif; font-weight: 400; fill: var(--ink-light); }
  .joiner-star { font-family: "Libre Caslon Text", serif; fill: var(--ink-light); }
  .subtitle { font-family: "Libre Caslon Text", serif; font-size: 35px; fill: var(--ink-light); }
  .author { font-family: "Bodoni Moda", serif; font-weight: 400; font-size: 58px; fill: var(--ink-light); }
  .author-credit { font-family: "Libre Caslon Text", serif; font-size: 11.5px; letter-spacing: 2px; fill: var(--ink-light); }
</style>
</head>
<body>
<svg class="canvas" viewBox="0 0 1200 1200" xmlns="http://www.w3.org/2000/svg">
  <defs>
    <linearGradient id="flagTone" x1="0" y1="0" x2="0.35" y2="1">
      <stop offset="0" stop-color="var(--navy-light)"/>
      <stop offset="0.28" stop-color="#2a3a7e"/>
      <stop offset="0.45" stop-color="var(--maroon)"/>
      <stop offset="0.62" stop-color="#2a3470"/>
      <stop offset="0.8" stop-color="var(--navy)"/>
      <stop offset="1" stop-color="var(--navy-deep)"/>
    </linearGradient>
    <radialGradient id="flagSheen" cx="0.35" cy="0.3" r="0.55">
      <stop offset="0" stop-color="var(--slate)" stop-opacity="0.45"/>
      <stop offset="1" stop-color="var(--slate)" stop-opacity="0"/>
    </radialGradient>
  </defs>

  <g class="cover">
    <g class="cover-art" role="img" aria-label="Waving American flag with white stars on blue and red and white stripes">
      <rect x="221" y="31" width="758" height="1137" fill="url(#flagTone)"/>
      <rect x="221" y="31" width="758" height="1137" fill="url(#flagSheen)"/>
    </g>

    <g class="title">
      <text class="title-word" x="274" y="570" font-size="138" textLength="666" lengthAdjust="spacingAndGlyphs">FREEDOM</text>

      <line x1="274" y1="611" x2="463" y2="611" stroke="var(--rule-light)" stroke-width="1.5"/>
      <line x1="750" y1="611" x2="940" y2="611" stroke="var(--rule-light)" stroke-width="1.5"/>
      <text class="joiner-star" x="474" y="620" font-size="24" letter-spacing="2">★★★</text>
      <text class="title-joiner" x="607" y="631" font-size="58" text-anchor="middle" textLength="68" lengthAdjust="spacingAndGlyphs">TO</text>
      <text class="joiner-star" x="655" y="620" font-size="24" letter-spacing="2">★★★</text>

      <text class="title-word" x="274" y="823" font-size="245" textLength="667" lengthAdjust="spacingAndGlyphs">ENJOY</text>
    </g>

    <g class="subtitle-block">
      <line x1="280" y1="881" x2="918" y2="881" stroke="var(--rule-red)" stroke-width="2"/>
      <text class="subtitle" x="600" y="921" text-anchor="middle" textLength="640" lengthAdjust="spacingAndGlyphs">Making Your Savings Last When Work Ends</text>
      <text class="subtitle" x="600" y="963" text-anchor="middle">and the Next Chapter Starts</text>
      <line x1="280" y1="989" x2="918" y2="989" stroke="var(--rule-red)" stroke-width="2"/>
    </g>

    <g class="byline">
      <text class="author" x="600" y="1095" text-anchor="middle" textLength="575" lengthAdjust="spacingAndGlyphs">DANIEL WHITMORE</text>
      <text class="author-credit" x="600" y="1124" text-anchor="middle" textLength="585" lengthAdjust="spacing">HOST OF THE STEADY HARBOR PODCAST AND NEXT CHAPTER RADIO</text>
    </g>
  </g>
</svg>
</body>
</html>
```